Business Card Design

I need a business card design for a new company based in Australind, Western Australia. The business is for puppet shows at children's parties, fetes, custom puppet builds, etc.Attached is a picture of Ray Pellow in silhouette. I was thinking a design of a puppeteer at the top of some stairs talking to a puppet in silhouette but open to suggestions. (Lantern Loft is named as I do all my puppet builds in the top room of my house (at the Lantern Loft).

Industry/Entity Type

Business

Contact Information for Business Card

Lantern Loft Marionettes, Dale Voss, Puppeteer / Puppet Builder, phone - 0438562703, Puppet shows / Custom Puppet Builds, Working With Children

Requirements
Must have
• Name and Logo on one side. Second side to have business card details.

```html
<!DOCTYPE html>
<html lang="en">
<head>
<meta charset="utf-8">
<title>Lantern Loft Marionettes – Business Card</title>
<link href="https://fonts.googleapis.com/css2?family=Source+Sans+3:ital,wght@0,400;0,600;1,400&display=swap" rel="stylesheet">
<style>
  :root {
    --maroon: #5f0a2c;
    --ink: #1c1c1c;
    --text: #3a3a3a;
    --paper: #fbfbfb;
    --backdrop: #4a4a4a;
    --white: #ffffff;
  }
  * { margin: 0; padding: 0; box-sizing: border-box; }
  html, body {
    width: 1200px; height: 750px; overflow: hidden;
    background: var(--backdrop);
    font-family: "Source Sans 3", "Myriad Pro", sans-serif;
  }
  .stage { position: relative; width: 1200px; height: 750px; }

  .card { position: absolute; left: 371px; width: 461px; height: 263px; overflow: hidden; }

  /* Front */
  .card-front { top: 107px; background: var(--paper); }
  .brand-name {
    position: absolute; left: 26px; top: 24px; width: 170px;
    font-weight: 600; font-size: 25px; line-height: 27px;
    color: var(--maroon);
  }
  .person { position: absolute; right: 24px; top: 132px; text-align: right; }
  .person-name { font-weight: 600; font-size: 18px; line-height: 20px; color: var(--maroon); }
  .person-role { font-size: 13px; line-height: 16px; color: var(--ink); }
  .rule { position: absolute; left: 26px; top: 160px; width: 255px; height: 1px; background: var(--ink); }
  .tab {
    position: absolute; right: 0; top: 130px; width: 8px; height: 37px;
    background: var(--maroon); border-radius: 19px 0 0 19px;
  }
  .services { position: absolute; right: 24px; top: 177px; list-style: none; text-align: right; }
  .services li {
    font-style: italic; font-size: 12px; line-height: 17.5px; color: var(--text);
  }
  .services li::after {
    content: ""; display: inline-block; width: 5px; height: 5px; border-radius: 50%;
    background: var(--maroon); margin-left: 8px; vertical-align: middle;
  }
  .contact { position: absolute; left: 25px; top: 194px; list-style: none; }
  .contact li {
    display: flex; align-items: center; gap: 6px;
    font-size: 12px; line-height: 17.5px; color: var(--text);
  }
  .contact svg { width: 11px; height: 11px; fill: var(--maroon); }
  .band { position: absolute; left: 0; bottom: 0; width: 100%; height: 13px; }

  /* Back */
  .card-back {
    top: 396px; background: var(--maroon);
    display: flex; align-items: center; justify-content: center;
  }
  .card-back .brand-name {
    position: static; width: auto; text-align: center;
    font-size: 38px; line-height: 40px; color: var(--white);
  }
</style>
</head>
<body>
<main class="stage">
  <section class="card card-front">
    <div class="brand-name">Lantern Loft<br>Marionettes</div>

    <div class="person">
      <p class="person-name">Dale Voss</p>
      <p class="person-role">Puppeteer / Puppet Builder</p>
    </div>
    <div class="rule"></div>
    <div class="tab"></div>

    <ul class="services">
      <li>Puppet shows</li>
      <li>Custom Puppet Builds</li>
      <li>Working With Children - 3917526</li>
    </ul>

    <ul class="contact">
      <li>
        <svg viewBox="0 0 24 24" aria-hidden="true"><path d="M6.6 10.8c1.4 2.8 3.8 5.1 6.6 6.6l2.2-2.2c.3-.3.7-.4 1-.2 1.1.4 2.3.6 3.6.6.6 0 1 .4 1 1V20c0 .6-.4 1-1 1C10.6 21 3 13.4 3 4c0-.6.4-1 1-1h3.5c.6 0 1 .4 1 1 0 1.3.2 2.5.6 3.6.1.3 0 .7-.2 1L6.6 10.8z"/></svg>
        0438562703
      </li>
      <li>
        <svg viewBox="0 0 24 24" aria-hidden="true"><path d="M2 5h20v14H2V5zm2 2v.5l8 5 8-5V7H4zm16 2.8l-8 5-8-5V17h16V9.8z"/></svg>
        hello@lanternloft.example
      </li>
    </ul>

    <svg class="band" viewBox="0 0 461 13" preserveAspectRatio="none" aria-hidden="true">
      <rect x="0" y="0" width="461" height="13" fill="var(--ink)"/>
      <polygon points="0,0 304,0 300,13 0,13" fill="var(--maroon)"/>
      <polygon points="304,0 306.5,0 302.5,13 300,13" fill="var(--white)"/>
    </svg>
  </section>

  <section class="card card-back">
    <div class="brand-name">Lantern Loft<br>Marionettes</div>
  </section>
</main>
</body>
</html>
```